Rug Cleaning Web Design Project

We need a web design for our cleaning company. We currently have a web page but are not happy with its design. We currently offer fine rug cleaning,upholstery cleaning, and residential and commercial carpet cleanning. We also offer water damage restoration. For our rug cleaning services we offer : Enzyme treatments for pet contamination and odor removal, application of stain protection that is designed for the fine textiles used in rug construction, application of treatments designed to prevent moth damage and pads designed to be used under rugs.Our current web site is harborfreshcare.example. We are intrested in a design with similar information to the web page of Velmora Rug Cleaners INC. We would like to use the colors that are present in our logo that will be uploaded with this description. We would also like this new page to be linked to our other address loomrinsepro.example. We would like the deign to be visually attractive but not "too busy".
Updates

Please include pictures of rugs, or people washing rugs if possible. We do not offer maid type cleaning services. We would not be interested in designs including pictures depicting that type service. Thanks for your hard work on this project.

Dana Whitlow

Industry/Entity Type

Residential

Requirements
Must have
• This page must be viewable on smart phones and tablets.

```html
<!DOCTYPE html>
<html lang="en">
<head>
<meta charset="utf-8">
<meta name="viewport" content="width=873">
<title>Harborfresh Care – Rug, Carpet &amp; Upholstery Cleaning</title>
<link href="https://fonts.googleapis.com/css2?family=Arimo:wght@400;700&family=Open+Sans:wght@400;600;700&family=Roboto+Condensed:wght@700&family=Lora:ital@1&display=swap" rel="stylesheet">
<style>
:root{
  --blue:#0b6fd6;
  --blue-bright:#1d8cf0;
  --blue-dark:#0d2fa8;
  --teal:#1784a8;
  --green:#4caf20;
  --tick:#8cc63f;
  --ink:#1a1a1a;
  --muted:#555;
  --line:#cfcfcf;
  --field:#efefef;
  --footer:#f2f2f2;
  --footer-side:#e9e9e9;
}
*{box-sizing:border-box;margin:0;padding:0}
html,body{width:873px;height:1200px;overflow:hidden;background:#fff}
body{position:relative;font-family:"Open Sans",Arial,sans-serif;color:var(--ink)}
.abs{position:absolute}
a{color:inherit;text-decoration:none}

/* page background fade (sits behind all content) */
.page-fade{left:0;top:940px;width:873px;height:76px;background:linear-gradient(#fff,#ececec)}

/* header */
.brand{left:110px;top:22px;display:flex;align-items:center;gap:10px}
.brand-mark{width:40px;height:40px;border-radius:50%;background:var(--teal)}
.brand-name{font:700 26px/1 "Open Sans",sans-serif;color:var(--teal);letter-spacing:-.3px}
.search{left:547px;top:31px;width:218px;height:31px;border-radius:5px;background:linear-gradient(#e6e6e6,#d9d9d9);border:1px solid #cfcfcf;font-size:10px;color:#888;padding:9px 0 0 17px}
.search-btn{position:absolute;right:2px;top:1px;width:27px;height:27px;border-radius:4px;background:linear-gradient(#3a9af0,#0c5fbf)}
.nav{left:109px;top:80px;width:658px;height:30px;border-radius:3px;background:linear-gradient(#2b93f5,#0a6ae0);display:flex;font:11px/30px Arimo,Arial,sans-serif;color:#fff}
.nav a{border-right:1px solid #3f8ee6;text-align:center;white-space:nowrap}
.nav .active{background:linear-gradient(#1b3fc0,#0c2898);border-radius:3px 0 0 3px}

/* hero */
.hero{left:110px;top:118px;width:658px;height:274px;background:#fff;box-shadow:0 1px 5px rgba(0,0,0,.3);overflow:hidden}
.hero-photo{position:absolute;right:0;top:0;width:400px;height:274px;background:linear-gradient(90deg,#fff 0%,#f1f3f4 30%,#e7e9ea 60%,#dfe1e2 100%)}
.hero-list{position:absolute;left:36px;top:17px;list-style:none}
.hero-list li{display:flex;align-items:center;height:34.3px;font:17px Arimo,Arial,sans-serif;color:var(--blue);white-space:nowrap}
.hero-list svg{margin-right:14px}

/* features */
.feature{top:408px;width:210px}
.feature-icon{position:absolute;left:0;top:0;width:52px;height:52px;border-radius:50%}
.feature h3{position:absolute;left:58px;top:3px;font:700 16px "Open Sans",sans-serif;color:var(--blue);white-space:nowrap}
.feature p{position:absolute;left:60px;top:26px;font:8px/12px Arimo,Arial,sans-serif;width:175px}
.more{font:700 8px Arimo,sans-serif;color:var(--blue);text-decoration:underline;letter-spacing:.2px}
.feature .more{position:absolute;left:60px;top:55px}
.band{left:110px;top:488px;width:658px;height:6px;background:radial-gradient(ellipse at center,rgba(0,0,0,.12),transparent 70%)}

/* welcome */
.welcome{left:109px;top:514px;width:470px}
.welcome h1{font:700 13px "Roboto Condensed",sans-serif;color:var(--blue);margin-bottom:8px}
.welcome p{font:9px/15.5px Arimo,Arial,sans-serif}
.welcome .more{display:block;margin-top:4px}
.dotted{border-top:1px dashed var(--line)}

/* services */
.svc{width:230px;height:96px}
.svc-img{position:absolute;left:0;top:0;width:87px;height:88px}
.svc h4{position:absolute;left:96px;top:0;font:400 11.5px/16px "Open Sans",sans-serif;width:130px}
.svc p{position:absolute;left:96px;font:700 8px/12px Arimo,Arial,sans-serif;width:112px}
.svc .more{position:absolute;left:96px}

/* sidebar */
.side-head{font:400 16px "Open Sans",sans-serif;display:flex;align-items:center;gap:12px}
.quote{left:608px;top:538px;width:158px;font:italic 9.3px/16px Lora,serif;text-align:justify;color:#333}
.author{left:610px;top:627px;width:116px;font:700 8px/13px Arimo,sans-serif;text-align:right}
.field{left:606px;width:166px;height:21px;background:var(--field);border-bottom:1px solid #ddd;font-size:8px;padding:6px 0 0 8px;color:#333}
.btn{left:672px;top:822px;width:99px;height:25px;border-radius:3px;background:linear-gradient(#2a9cf5,#0a66d4);border:1px solid #58b04a;color:#fff;font:700 10px/23px Arimo,sans-serif;text-align:center}
.address{left:608px;top:876px;font:8px/13.2px Arimo,Arial,sans-serif}
.address h5{font:700 9px "Roboto Condensed",sans-serif;color:#444;margin-bottom:6px}

/* footer */
.footer{left:0;top:1016px;width:873px;height:184px;background:var(--footer);border-top:1px solid #ddd}
.footer-side{left:605px;top:1016px;width:268px;height:184px;background:var(--footer-side);border-left:1px solid #d5d5d5}
.fcol h6{font:400 17px "Open Sans",sans-serif;color:#333;padding-bottom:8px;border-bottom:1px solid #e0e0e0;width:130px}
.fcol ul{list-style:none;margin-top:8px}
.fcol li{font-size:7.5px;letter-spacing:1px;line-height:18.2px;color:#444;white-space:nowrap}
.social{display:flex;gap:7px;margin-top:10px}
.social span{width:20px;height:20px}
.partner{font:700 15px "Open Sans",sans-serif;color:var(--teal);text-align:center;width:268px;left:605px}
.copy{left:605px;width:268px;top:1086px;text-align:center;font-size:7.5px;line-height:12.5px;letter-spacing:.3px}
</style>
</head>
<body>

<div class="abs page-fade"></div>

<header>
  <div class="abs brand"><span class="brand-mark"></span><span class="brand-name">Harborfresh Care</span></div>
  <div class="abs search">Search from this site<span class="search-btn"></span></div>
  <nav class="abs nav">
    <a class="active" style="width:66px">Home</a>
    <a style="width:65px">About Us</a>
    <a style="width:88px">Rug Cleaning</a>
    <a style="width:94px">Carpet Cleaning</a>
    <a style="width:114px">Upholstery Cleaning</a>
    <a style="width:150px">Water Damage Restoration</a>
    <a style="width:81px;border:0">Contact Us</a>
  </nav>
</header>

<section class="abs hero">
  <div class="hero-photo" role="img" aria-label="Cleaning professional in red apron and yellow gloves giving a thumbs up in a bright room"></div>
  <ul class="hero-list">
    <li><svg width="18" height="20" viewBox="0 0 18 20"><path d="M1 11l5 6L17 2" fill="none" stroke="var(--tick)" stroke-width="4" stroke-linecap="round"/></svg>Carpet Cleanning</li>
    <li><svg width="18" height="20" viewBox="0 0 18 20"><path d="M1 11l5 6L17 2" fill="none" stroke="var(--tick)" stroke-width="4" stroke-linecap="round"/></svg>Upholstery Cleaning</li>
    <li><svg width="18" height="20" viewBox="0 0 18 20"><path d="M1 11l5 6L17 2" fill="none" stroke="var(--tick)" stroke-width="4" stroke-linecap="round"/></svg>Rug Cleanning</li>
    <li><svg width="18" height="20" viewBox="0 0 18 20"><path d="M1 11l5 6L17 2" fill="none" stroke="var(--tick)" stroke-width="4" stroke-linecap="round"/></svg>Moth Damage Prevent</li>
    <li><svg width="18" height="20" viewBox="0 0 18 20"><path d="M1 11l5 6L17 2" fill="none" stroke="var(--tick)" stroke-width="4" stroke-linecap="round"/></svg>Pet Contamination Removal</li>
    <li><svg width="18" height="20" viewBox="0 0 18 20"><path d="M1 11l5 6L17 2" fill="none" stroke="var(--tick)" stroke-width="4" stroke-linecap="round"/></svg>Stain Protection for Rugs</li>
    <li><svg width="18" height="20" viewBox="0 0 18 20"><path d="M1 11l5 6L17 2" fill="none" stroke="var(--tick)" stroke-width="4" stroke-linecap="round"/></svg>Water Damage Restoration</li>
  </ul>
</section>

<section>
  <div class="abs feature" style="left:110px">
    <div class="feature-icon" role="img" aria-label="Blue globe with red check mark" style="background:radial-gradient(circle at 35% 35%,#4ea6f0,#0c4fa8)"></div>
    <h3>Our Service</h3>
    <p>Lorem ipsum dolor sit amet, consectetur adipiscing elit.</p>
    <a class="more">LEARN MORE</a>
  </div>
  <div class="abs feature" style="left:337px">
    <div class="feature-icon" role="img" aria-label="Green and blue refresh arrows" style="background:radial-gradient(circle at 40% 40%,#2a3a4a,#0a1218)"></div>
    <h3>How Fresh It</h3>
    <p>Lorem ipsum dolor sit amet, consectetur adipiscing elit.</p>
    <a class="more">LEARN MORE</a>
  </div>
  <div class="abs feature" style="left:553px">
    <div class="feature-icon" role="img" aria-label="Office building with shrub" style="border-radius:4px;width:46px;background:linear-gradient(90deg,#9aa6ad,#dfe5e8,#7c8a92)"></div>
    <h3 style="left:52px">Our Company</h3>
    <p style="left:54px">Lorem ipsum dolor sit amet, consectetur adipiscing elit.</p>
    <a class="more" style="left:54px">LEARN MORE</a>
  </div>
  <div class="abs band"></div>
</section>

<main>
  <article class="abs welcome">
    <h1>WELCOME TO HARBORFRESH CARE</h1>
    <p>We are offering you the joy of a sparkling clean home, washed by hand using our innovative low pressure cleaning system. Your house is given a comprehensive wash from the gutters down, including eaves, walls, windows, frames, screens, etc. The resulting look is, like new appearance. It can also be used for revitalizing</p>
    <a class="more">LEARN MORE</a>
  </article>
  <div class="abs dotted" style="left:109px;top:613px;width:464px"></div>

  <div class="abs svc" style="left:109px;top:632px">
    <div class="svc-img" role="img" aria-label="Carpet cleaning wand on beige carpet" style="background:linear-gradient(135deg,#cfc8bd,#8e8478)"></div>
    <h4>Carpet Cleaning</h4>
    <p style="top:19px">Integer faucibus massa id ante convallis aliquet. Fusce ullamcorper, lectus ut ueum risus lorem vel ligula. Sed</p>
    <a class="more" style="top:77px">LEARN MORE</a>
  </div>
  <div class="abs svc" style="left:350px;top:632px">
    <div class="svc-img" role="img" aria-label="Hand cleaning white sofa cushion" style="background:linear-gradient(135deg,#e8e4dc,#6a5d50)"></div>
    <h4>Upholstery Cleaning</h4>
    <p style="top:19px">Integer faucibus massa id ante convallis aliquet. Fusce ullamcorper, lectus ut ueum risus lorem vel ligula. Sed</p>
    <a class="more" style="top:77px">LEARN MORE</a>
  </div>
  <div class="abs svc" style="left:109px;top:749px">
    <div class="svc-img" role="img" aria-label="Baby crawling on a soft rug" style="background:linear-gradient(135deg,#d9cfc4,#b0a494)"></div>
    <h4>Rug Cleaning</h4>
    <p style="top:17px">Integer faucibus massa id ante convallis aliquet. Fusce ullamcorper, lectus ut ueum risus lorem vel ligula. Sed</p>
    <a class="more" style="top:75px">LEARN MORE</a>
  </div>
  <div class="abs svc" style="left:350px;top:749px">
    <div class="svc-img" role="img" aria-label="Puppy lying on tiled floor beside a mop" style="background:linear-gradient(135deg,#e6e1d8,#9b8f80)"></div>
    <h4>Pet Contamination Removal</h4>
    <p style="top:35px">Integer faucibus massa id ante convallis aliquet. mollis. Nam cursus libero</p>
    <a class="more" style="top:75px">LEARN MORE</a>
  </div>
  <div class="abs svc" style="left:109px;top:865px">
    <div class="svc-img" role="img" aria-label="Close-up of a red patterned rug" style="background:linear-gradient(135deg,#b5553a,#6f3a2a)"></div>
    <h4>Moth Damage Prevent</h4>
    <p style="top:16px">Integer faucibus massa id ante convallis aliquet. Fusce ullamcorper, lectus ut ueum risus lorem vel ligula. Sed</p>
    <a class="more" style="top:75px">LEARN MORE</a>
  </div>
  <div class="abs svc" style="left:350px;top:865px">
    <div class="svc-img" role="img" aria-label="Flooded office hallway with cleaning equipment" style="background:linear-gradient(135deg,#a86f3c,#4f3a28)"></div>
    <h4>Water Damage Restoration</h4>
    <p style="top:35px">Integer faucibus massa id ante convallis aliquet. mollis. Nam cursus libero</p>
    <a class="more" style="top:75px">LEARN MORE</a>
  </div>
</main>

<aside>
  <div class="abs side-head" style="left:608px;top:502px">
    <svg width="20" height="20" viewBox="0 0 20 20"><path d="M10 2C5 2 1.5 5 1.5 9c0 2.3 1.2 4.2 3 5.4L4 18l4-2.3c.6.1 1.3.2 2 .2 5 0 8.5-3 8.5-6.9S15 2 10 2z" fill="#9fd0f2" stroke="#5aa7dc"/></svg>Testimonials
  </div>
  <div class="abs dotted" style="left:608px;top:530px;width:160px;border-color:#e4e4e4"></div>
  <p class="abs quote">“ Lorem ipsum dolor sit amet, consectetur adipiscing elit. Ut ac orci tellus, vestibulum mollis sem. Nullam rhoncus lacus eu mi consequat consequat. ”</p>
  <p class="abs author">- Telric, President Manager<br>Clean residence</p>
  <div class="abs" role="img" aria-label="Customer portrait" style="left:732px;top:621px;width:31px;height:32px;background:linear-gradient(#8a8a8a,#4a4a4a)"></div>
  <div class="abs dotted" style="left:607px;top:668px;width:160px"></div>

  <div class="abs side-head" style="left:608px;top:679px">
    <span style="width:20px;height:20px;background:#e0402a;border-radius:3px"></span>Subscribe
  </div>
  <div class="abs dotted" style="left:608px;top:708px;width:160px;border-color:#e4e4e4"></div>
  <p class="abs" style="left:608px;top:723px;font:700 8.3px/13px Arimo,sans-serif">Sign Up For Our Newsletter And<br>You Will Get Free Tips To Your Inbox!</p>
  <div class="abs field" style="top:757px">Name</div>
  <div class="abs field" style="top:790px">Email Adress</div>
  <div class="abs btn">Yes please!</div>
  <div class="abs dotted" style="left:607px;top:865px;width:164px"></div>

  <div class="abs address">
    <h5>HARBORFRESH CARE</h5>
    Street Name Number 123-456<br>City, Country<br>Phone: 00 1234 567<br>Mobile: 00 1234 567<br>Email: info@harborfreshcare.example
  </div>
</aside>

<footer>
  <div class="abs footer"></div>
  <div class="abs footer-side"></div>

  <div class="abs fcol" style="left:108px;top:1033px">
    <h6>Our Sites</h6>
    <ul><li>About Us</li><li>Rug Cleaning</li><li>Carpet Cleaning</li><li>Upholstery Cleaning</li><li>Water Damage Restoration</li><li>Contact Us</li></ul>
  </div>
  <div class="abs fcol" style="left:265px;top:1033px">
    <h6>Our Services</h6>
    <ul><li>Carpet Cleaning</li><li>Upholstery Cleaning</li><li>Rug Cleaning</li><li>Pet Contamination Removal</li><li>Moth Damage Prevent</li><li>Water Damage Restoration</li></ul>
  </div>
  <div class="abs fcol" style="left:449px;top:1033px">
    <h6>Follow us</h6>
    <div class="social">
      <span role="img" aria-label="Social network link" style="background:#3b5998"></span>
      <span role="img" aria-label="Social network link" style="background:#3fa9e6"></span>
      <span role="img" aria-label="Video channel link" style="background:#c4302b"></span>
    </div>
  </div>

  <div class="abs partner" style="top:1045px">Brightside House Washing</div>
  <p class="abs copy">Copyright 2012 Harborfresh Care<br>All Rights Reserved</p>
  <div class="abs partner" style="top:1128px;color:#1f4f86">LoomRinsePro</div>
</footer>

</body>
</html>
```